Employment and Trade Show Banner for Senior Living Solutions

We are looking to create a new sign for employment fairs and trade shows to promote our senior living campus and attract potential employees as well positively promote our campus to potential residents/tenants. We serve a variety of seniors at a variety of different care levels including: long-term care, rehabilitation, locked dementia care unit, assisted living, and independent living. The sign dimensions are 33" x 80". Our website is www.silverpinesnorland.com.

We are looking for something catchy and professional.

Our Vision: Silverpines of Norland offers a variety of senior services which include: Independent Living, Assisted Living, Rehabilitative Care, Skilled Nursing Care, and Memory Care. Our team provides the quality services you should expect in senior care.

Our Campus is made up of 4 different facilities: Marlowfield Care Center, OakMeadow Village, Willow Lodge, and Juniper Terrace. Perhaps advertising these somehow under our umbrella name of Silverpines of Norland?

Target Market(s)

Attract potential employees as well positively promote our campus to potential residents/tenants who may need care in the future.

Industry/Entity Type

Trade

Requirements
Must have
• Logo
Nice to have
• Our Campus is made up of 4 different facilities: Marlowfield Care Center, OakMeadow Village, Willow Lodge, and Juniper Terrace. Perhaps advertising these somehow under our umbrella name of Silverpines of Norland?
• Perhaps something based around our vision?
• Our Vision: Silverpines of Norland offers a variety of senior services which include: Independent Living, Assisted Living, Rehabilitative Care, Skilled Nursing Care, and Memory Care. Our team provides the quality services you should expect in senior care.

```html
<!DOCTYPE html>
<html lang="en">
<head>
<meta charset="utf-8">
<title>Silverpines of Norland – Roll-up Banner</title>
<link href="https://fonts.googleapis.com/css2?family=Open+Sans:wght@400;600;700&display=swap" rel="stylesheet">
<style>
  :root {
    --forest: #146b35;
    --forest-dark: #0f5a2b;
    --orange: #e07420;
    --ink: #444444;
    --ink-dark: #333333;
    --rule: #7a7a7a;
    --page: #e9eaeb;
    --white: #ffffff;
  }
  * { margin: 0; padding: 0; box-sizing: border-box; }
  html, body {
    width: 1200px; height: 960px; overflow: hidden;
    background: var(--page);
    font-family: "Open Sans", sans-serif;
  }
  .banner {
    position: absolute;
    left: 402px; top: 1px;
    width: 395px; height: 957px;
    background: var(--white);
    overflow: hidden;
    transform: scale(0.94);
    transform-origin: center center;
    box-shadow: 0 6px 18px rgba(0,0,0,0.18);
  }
  .banner-art { position: absolute; left: 0; top: 0; }
  .brand {
    position: absolute; left: 40px; top: 160px;
    display: flex; align-items: center; gap: 8px;
    color: var(--forest-dark);
    font-weight: 400; font-size: 19px; letter-spacing: 1px;
  }
  .brand-dot {
    width: 22px; height: 22px; border-radius: 50%;
    background: var(--forest-dark);
  }
  .tagline {
    position: absolute; left: 38px; top: 224px;
    font-size: 21px; line-height: 25px; color: var(--ink-dark);
  }
  .intro {
    position: absolute; left: 0; right: 0; top: 572px;
    text-align: center; font-size: 15px; line-height: 18px; color: var(--ink);
  }
  .services {
    position: absolute; left: 26px; right: 30px;
    display: flex; justify-content: center;
    color: var(--forest); font-weight: 600; font-size: 12px; line-height: 14px;
    text-align: center;
  }
  .service { padding: 1px 6px 3px; white-space: nowrap; }
  .service + .service { border-left: 1px solid var(--rule); }
  .services-top { top: 622px; border-bottom: 1px solid var(--rule); justify-content: space-between; }
  .services-bottom { top: 665px; }
  .services-bottom .service { padding: 1px 30px 3px; }
  .headline {
    position: absolute; left: 0; right: 0; top: 708px;
    text-align: center; color: var(--orange);
    font-weight: 700; font-size: 20px; letter-spacing: -0.2px;
  }
  .about {
    position: absolute; left: 20px; right: 20px; top: 745px;
    text-align: center; font-size: 11px; line-height: 14.6px; color: var(--ink);
  }
  .web {
    position: absolute; left: 0; right: 0; top: 816px;
    display: flex; justify-content: center; align-items: center; gap: 8px;
    font-weight: 700; font-size: 18px; color: var(--ink-dark);
  }
</style>
</head>
<body>
  <div class="banner">
    <svg class="banner-art" width="395" height="957" viewBox="0 0 395 957">
      <defs>
        <linearGradient id="heroTone" x1="0" y1="0" x2="0" y2="1">
          <stop offset="0" stop-color="#f0efe9"/>
          <stop offset="0.35" stop-color="#dedbcc"/>
          <stop offset="0.55" stop-color="#aeab96"/>
          <stop offset="0.78" stop-color="#59604a"/>
          <stop offset="1" stop-color="#6d8f3b"/>
        </linearGradient>
        <linearGradient id="handsTone" x1="0" y1="0" x2="1" y2="1">
          <stop offset="0" stop-color="#c9b3a6"/>
          <stop offset="1" stop-color="#8f8275"/>
        </linearGradient>
        <clipPath id="bannerClip"><rect width="395" height="957"/></clipPath>
      </defs>
      <rect class="top-band" width="395" height="140" fill="var(--forest)"/>
      <circle cx="196" cy="292" r="258" fill="url(#heroTone)" role="img"
              aria-label="Photo: caregiver pushing a senior in a wheelchair across a grassy field at sunset"/>
      <circle cx="338" cy="80" r="14" fill="var(--white)"/>
      <circle cx="61" cy="511" r="33" fill="var(--orange)"/>
      <g clip-path="url(#bannerClip)">
        <circle cx="282" cy="950" r="92" fill="url(#handsTone)" role="img"
                aria-label="Photo: close-up of an elderly person's folded hands"/>
      </g>
      <circle cx="198" cy="916" r="13" fill="var(--orange)"/>
    </svg>

    <div class="brand"><span class="brand-dot"></span><span>Silverpines of Norland</span></div>
    <p class="tagline">Creatively providing<br>a caring community</p>

    <p class="intro">We serve a variety of seniors at a variety of<br>different care levels including</p>

    <div class="services services-top">
      <span class="service">Skilled Nursing<br>Care</span>
      <span class="service">Short Term<br>Rehabilitative Care</span>
      <span class="service">Secure Memory<br>Care</span>
    </div>
    <div class="services services-bottom">
      <span class="service">Assisted Living<br>Communities</span>
      <span class="service">Independent<br>Senior Living</span>
    </div>

    <h2 class="headline">CREATIVE . CARING . COMMUNITIES</h2>

    <p class="about">Silverpines of Norland consists of four Communities offering a variety of neighborhoods for senior living. Each of these communities offers services along with compassionate, caring environments to meet each of our resident's needs.</p>

    <div class="web">
      <svg width="14" height="14" viewBox="0 0 14 14" aria-hidden="true">
        <g fill="none" stroke="var(--forest)" stroke-width="1.2">
          <circle cx="7" cy="7" r="6"/>
          <ellipse cx="7" cy="7" rx="2.6" ry="6"/>
          <line x1="1" y1="7" x2="13" y2="7"/>
          <line x1="2" y1="4" x2="12" y2="4"/>
          <line x1="2" y1="10" x2="12" y2="10"/>
        </g>
      </svg>
      <span>www.silverpinesnorland.com</span>
    </div>
  </div>
</body>
</html>
```